Quartz Meridian Business Card Design

I need a 2-sided business card for my computer engineering consulting company. The card is expected to convey a message of cutting edge forward thinking, and boldnes. I would like the card to be memorable and stand-out on a desk. The card should be bold, modern, clean, and highly professional. I am a big fan of watermarks/shadows and other intersting but restrained uses of the logo. The card can be a shape other than the traditional rectangle. Perhaps a rectangle with rounded edges. All I ask is the card be able to fit into a standard wallet. I will supply two logos, one with a red background, and one with a black background. Please feel free to work with both of these logos.
Updates

Hi all, thank you for your submissions. I will post the original vector file later today. Thank you for your patience.

Regards,

Henry

Target Market(s)

Engineering Buyers, Vice Presidents and Directors

Industry/Entity Type

Computer

Requirements
Must have
• 2 sides

```html
<!DOCTYPE html>
<html lang="en">
<head>
<meta charset="utf-8">
<title>Quartz Meridian Works – Business Card</title>
<link rel="stylesheet" href="https://fonts.googleapis.com/css2?family=Open+Sans:wght@600&family=Roboto:wght@400;700&display=swap">
<style>
  :root {
    --stage: #d6d6d4;
    --card: #0b0b0b;
    --red: #b3232a;
    --red-deep: #7e141a;
    --grey: #8c8c8c;
  }
  html, body {
    margin: 0;
    width: 1200px;
    height: 792px;
    overflow: hidden;
    background: var(--stage);
  }
  .canvas {
    position: relative;
    width: 1200px;
    height: 792px;
  }
  .card {
    position: absolute;
    top: 242px;
    width: 540px;
    height: 308px;
    background: var(--card);
    overflow: hidden;
  }
  .card--front { left: 40px; }
  .card--back { left: 620px; }

  /* Front side */
  .feature-art {
    position: absolute;
    left: 0;
    top: 96px;
    width: 250px;
    height: 212px;
    background: linear-gradient(160deg, var(--red) 0%, var(--red-deep) 100%);
  }
  .arrow-path {
    position: absolute;
    left: 0;
    top: 0;
  }
  .intro {
    position: absolute;
    right: 48px;
    top: 56px;
    text-align: right;
    font-family: "Roboto", Arial, sans-serif;
    color: var(--red);
  }
  .intro__greeting {
    margin: 0;
    font-size: 17px;
    font-weight: 400;
  }
  .intro__name {
    margin: 0;
    font-size: 32px;
    font-weight: 700;
    letter-spacing: -0.5px;
    line-height: 1.05;
  }
  .contact {
    position: absolute;
    right: 20px;
    top: 150px;
    margin: 0;
    padding: 0;
    list-style: none;
    font-family: "Roboto", Arial, sans-serif;
    font-size: 17px;
    color: var(--red);
  }
  .contact__item {
    display: flex;
    justify-content: flex-end;
    align-items: center;
    gap: 10px;
    height: 23px;
  }
  .contact__icon {
    width: 14px;
    height: 14px;
  }

  /* Back side */
  .brand {
    position: absolute;
    left: 0;
    right: 0;
    top: 104px;
    display: flex;
    flex-direction: column;
    align-items: center;
    font-family: "Open Sans", Arial, sans-serif;
    font-weight: 600;
  }
  .brand__row {
    display: flex;
    align-items: center;
    gap: 14px;
  }
  .brand__square {
    width: 42px;
    height: 42px;
    background: var(--red);
  }
  .brand__name {
    font-size: 27px;
    letter-spacing: 0.5px;
    color: var(--red);
    white-space: nowrap;
  }
  .brand__tagline {
    margin-top: 12px;
    font-size: 14px;
    letter-spacing: 4px;
    color: var(--grey);
    white-space: nowrap;
  }
</style>
</head>
<body>
<main class="canvas">

  <section class="card card--front" aria-label="Business card front">
    <div class="feature-art" role="img" aria-label="Large red decorative archer graphic on a red band"></div>
    <svg class="arrow-path" width="540" height="308" viewBox="0 0 540 308" aria-hidden="true">
      <path d="M262 96 Q 360 -6 470 16 Q 490 22 480 42" fill="none" stroke="#b3232a" stroke-width="2" stroke-dasharray="3 4"/>
      <path d="M473 38 L480 48 L487 38" fill="none" stroke="#b3232a" stroke-width="2"/>
    </svg>

    <div class="intro">
      <p class="intro__greeting">Hi! I'm</p>
      <h1 class="intro__name">Marcus VALE</h1>
    </div>

    <ul class="contact">
      <li class="contact__item">+00 987 654 321
        <svg class="contact__icon" viewBox="0 0 14 14" aria-hidden="true"><rect x="4" y="1" width="6" height="12" rx="1" fill="none" stroke="#b3232a" stroke-width="1.5"/><rect x="5.5" y="3" width="3" height="3" fill="#b3232a"/></svg>
      </li>
      <li class="contact__item">marcus@qmworks.net
        <svg class="contact__icon" viewBox="0 0 14 14" aria-hidden="true"><rect x="1" y="3" width="12" height="8" fill="none" stroke="#b3232a" stroke-width="1.5"/><path d="M1 3 L7 8 L13 3" fill="none" stroke="#b3232a" stroke-width="1.5"/></svg>
      </li>
      <li class="contact__item">www.qmworks.net
        <svg class="contact__icon" viewBox="0 0 14 14" aria-hidden="true"><rect x="1" y="3" width="2" height="10" fill="#b3232a"/><rect x="4.5" y="6" width="2" height="7" fill="#b3232a"/><rect x="8" y="8" width="2" height="5" fill="#b3232a"/><rect x="11.5" y="10" width="2" height="3" fill="#b3232a"/></svg>
      </li>
    </ul>
  </section>

  <section class="card card--back" aria-label="Business card back">
    <div class="brand">
      <div class="brand__row">
        <span class="brand__square" aria-hidden="true"></span>
        <span class="brand__name">QUARTZ MERIDIAN WORKS LTD</span>
      </div>
      <span class="brand__tagline">BOLD IDEAS BUILT TO LAST</span>
    </div>
  </section>

</main>
</body>
</html>
```